Corvane Building Materials letterhead template

Simple but professional letterhead template for business communication.
LOGO/name in upper left, balanced by company contact info on right upper.
Subject description, date...
addressee, cc: and BC: if applicable editable info..

Need extra days to review

```html
<!DOCTYPE html>
<html lang="en">
<head>
<meta charset="utf-8">
<title>Corvane Building Materials – Letterhead</title>
<link href="https://fonts.googleapis.com/css2?family=Questrial&family=Roboto:wght@400&display=swap" rel="stylesheet">
<style>
  :root {
    --paper: #e2e2e2;
    --brand-blue: #0b57c5;
    --body-text: #5a5a5a;
    --contact-text: #4a4a4a;
    --rule: #b9b9b9;
  }
  html, body {
    margin: 0;
    padding: 0;
    width: 1023px;
    height: 1200px;
    overflow: hidden;
    background: var(--paper);
  }
  .letterhead {
    position: relative;
    width: 1023px;
    height: 1200px;
    background: var(--paper);
    font-family: "Questrial", "Century Gothic", sans-serif;
    color: var(--body-text);
  }
  .brand-name {
    position: absolute;
    left: 98px;
    top: 118px;
    margin: 0;
    font-family: "Questrial", "Century Gothic", sans-serif;
    font-weight: 400;
    font-size: 24px;
    line-height: 28px;
    color: var(--brand-blue);
  }
  .contact {
    position: absolute;
    left: 668px;
    top: 86px;
    padding: 6px 0 6px 22px;
    border-left: 1px solid var(--rule);
    font-family: "Roboto", sans-serif;
    font-size: 14.5px;
    line-height: 19px;
    color: var(--contact-text);
    font-style: normal;
  }
  .contact p { margin: 0; }
  .contact .address { margin-bottom: 7px; }
  .contact-line {
    display: flex;
    align-items: center;
    gap: 7px;
  }
  .contact-line svg { width: 12px; height: 12px; fill: var(--brand-blue); flex: none; }
  .letter {
    position: absolute;
    left: 98px;
    top: 385px;
    width: 840px;
  }
  .salutation {
    font-size: 19px;
    line-height: 24px;
    margin: 0 0 42px;
    color: #555;
  }
  .letter-body p {
    margin: 0 0 23px;
    font-size: 15.5px;
    line-height: 22px;
    text-align: justify;
    hyphens: auto;
  }
  .letter-body p.spaced { margin-top: 42px; }
  .closing {
    margin: 85px 0 0;
    font-size: 15.5px;
  }
</style>
</head>
<body>
<main class="letterhead">
  <header>
    <h1 class="brand-name">Corvane Building Materials</h1>
    <address class="contact">
      <p class="address">PO Box 318 Marlow Falls<br>Westerly 40917</p>
      <p class="contact-line">
        <svg viewBox="0 0 24 24" aria-hidden="true"><path d="M6.6 10.8a15.1 15.1 0 0 0 6.6 6.6l2.2-2.2a1 1 0 0 1 1-.25 11.4 11.4 0 0 0 3.6.57 1 1 0 0 1 1 1V20a1 1 0 0 1-1 1A17 17 0 0 1 3 4a1 1 0 0 1 1-1h3.5a1 1 0 0 1 1 1c0 1.25.2 2.45.57 3.57a1 1 0 0 1-.25 1z"/></svg>
        (555) 014.2260
      </p>
      <p class="contact-line">
        <svg viewBox="0 0 24 24" aria-hidden="true"><path d="M2 5h20v14H2z M2 5l10 8 10-8" fill="none" stroke="#0b57c5" stroke-width="2.5"/></svg>
        hello@corvanematerials.example
      </p>
      <p class="contact-line">
        <svg viewBox="0 0 24 24" aria-hidden="true"><circle cx="12" cy="12" r="10"/><path d="M2 12h20M12 2c3 3 3 17 0 20M12 2c-3 3-3 17 0 20" fill="none" stroke="#e2e2e2" stroke-width="1.5"/></svg>
        www.corvanematerials.example
      </p>
    </address>
  </header>

  <section class="letter">
    <p class="salutation">Dear Martin,</p>
    <div class="letter-body">
      <p>Donec malesuada orci vitae nulla accumsan porta a id massa. Quisque accumsan iaculis magna sit amet fringilla. Maecenas consequat, magna eget tincidunt semper, odio nibh rutrum mi, id feugiat ante nisi eu risus. Vestibulum nunc orci, rhoncus a placerat in, ultricies in mi. Cras mattis varius eros, vel fringilla nisi suscipit eget. Quisque scelerisque sagittis nulla at porttitor.</p>
      <p>Lorem ipsum dolor sit amet, consectetur adipiscing elit. Donec orci purus, luctus vitae dignissim eu, iaculis sed purus. Vivamus faucibus, ipsum nec aliquet viverra, leo mauris condimentum ligula, sit amet sagittis enim ligula quis arcu. Nam egestas tortor id nisi porttitor mattis. In tortor ante, ultricies in suscipit a, tempus non massa. Vivamus et auctor mi. Fusce vel massa nulla. Phasellus nec eros mauris, et scelerisque orci.</p>
      <p class="spaced">It is a long established fact that a reader will be distracted by the readable content of a page when looking at its layout. The point of using Lorem Ipsum is that it has a more-or-less normal distribution of letters, as opposed to using 'Content here, content here', making it look like readable English. Many desktop publishing packages</p>
      <p>Sed id augue vitae urna euismod commodo aliquet a quam. Pellentesque arcu velit, cursus et malesuada ut, consequat et diam. Nullam erat sem, rhoncus id ullamcorper vitae, rhoncus et arcu. In ultricies ultricies nulla, ut rutrum nisi iaculis at. Donec eu magna a metus ornare faucibus. Fusce aliquet faucibus ultricies. Morbi semper, est id tincidunt gravida, sem arcu adipiscing lacus, ac bibendum nulla leo eu purus. Quisque nec diam sed risus consectetur a ccumsan quis quis nibh. Vestibulum id purus lorem.</p>
    </div>
    <p class="closing">Sincerely,</p>
  </section>
</main>
</body>
</html>
```